| ■お仕事内容 海外の高級ファッションブランドを販売するサイト用の無償修理保証のバナー製作をお願いいたします。 メンズ、レディースどちらも取り扱っているブランドのため、どちらでも使えるデザインが望ましいです。 ■バナーに記載する内容 「1年間無償修理保証」ということが伝わる文章を入れてください。 ※独自のサービスのため、「当店だけの・・・」など独自の付加価値サービスである文言を入れたいです。 ■重視する点 ・高級感のあるデザイン(ごちゃごちゃしていない、シンプルで目を引くもの) ・フラットデザインが基調になっているサイトにマッチするデザイン ・ファッション系のサイトに合うデザイン ・本物である安心感・信頼感のあるデザイン ■報酬 5,000円 ■応募条件 WEBサイトのバナー、アイコンなどの製作経験をお持ちの方 ご提案価格と実績のバランスを見てお仕事をお願いする方を選定させていただきます。 たくさんのご応募お待ちしております。 何卒宜しくお願いいたします。 |

```html
<!DOCTYPE html>
<html lang="ja">
<head>
<meta charset="utf-8">
<title>1年間無償修理保証</title>
<link rel="stylesheet" href="https://fonts.googleapis.com/css2?family=Noto+Serif+JP:wght@500;700;900&family=Zen+Maru+Gothic:wght@500;700&display=swap">
<style>
  :root {
    --paper: #ffffff;
    --frame: #b9b9b9;
    --gold-deep: #7a5a2e;
    --gold-mid: #b8955c;
    --gold-light: #ecdcb8;
    --ink: #151515;
    --crimson: #a3121a;
    --header-text: #ffffff;
  }
  * { margin: 0; padding: 0; box-sizing: border-box; }
  html, body {
    width: 1200px;
    height: 412px;
    overflow: hidden;
    background: var(--paper);
  }
  .banner {
    position: relative;
    width: 1200px;
    height: 412px;
    background: var(--paper);
  }
  .banner-frame {
    position: absolute;
    left: 40px;
    top: 24px;
    width: 1126px;
    height: 360px;
    border: 2px solid var(--frame);
    overflow: hidden;
    background: var(--paper);
  }
  .gold-band {
    position: absolute;
    left: 0;
    top: 0;
    width: 1122px;
    height: 200px;
  }
  .tagline {
    position: absolute;
    left: 0;
    right: 0;
    top: 42px;
    text-align: center;
    font-family: "Zen Maru Gothic", "Noto Serif JP", sans-serif;
    font-weight: 700;
    font-size: 54px;
    letter-spacing: 2px;
    color: var(--header-text);
    text-shadow: 0 1px 2px rgba(70, 45, 10, 0.35);
  }
  .headline {
    position: absolute;
    left: 30px;
    top: 182px;
    display: flex;
    align-items: baseline;
    font-family: "Noto Serif JP", serif;
    white-space: nowrap;
  }
  .headline-term {
    display: inline-block;
    font-weight: 700;
    font-size: 88px;
    color: var(--ink);
    transform: skewX(-12deg);
    letter-spacing: -2px;
    margin-right: 14px;
  }
  .headline-offer {
    display: inline-block;
    font-weight: 900;
    font-size: 112px;
    color: var(--crimson);
    letter-spacing: 2px;
    padding-bottom: 4px;
    border-bottom: 6px solid var(--crimson);
    line-height: 1.1;
  }
</style>
</head>
<body>
  <div class="banner">
    <div class="banner-frame">
      <svg class="gold-band" viewBox="0 0 1122 200" preserveAspectRatio="none" aria-hidden="true">
        <defs>
          <linearGradient id="goldSweep" x1="0" y1="0" x2="1" y2="0.2">
            <stop offset="0" stop-color="var(--gold-deep)"/>
            <stop offset="0.45" stop-color="var(--gold-mid)"/>
            <stop offset="1" stop-color="var(--gold-light)"/>
          </linearGradient>
        </defs>
        <path d="M0 0 H1122 V120 C980 140 860 150 720 140 C560 128 420 118 260 140 C170 152 80 165 0 168 Z" fill="url(#goldSweep)"/>
      </svg>
      <p class="tagline">当店だけの特別なサービス</p>
      <h1 class="headline">
        <span class="headline-term">1年間</span>
        <span class="headline-offer">無償修理保証</span>
      </h1>
    </div>
  </div>
</body>
</html>
```